Flyer für Anbieter einer Fortbildung für Beratungslehrer
Zielgruppe
Wir bieten eine Fortbildung für Beratungslehrer an, welche mit immer komplexer werdenden psychischen Fällen arbeiten. Diese Fortbildung setzt sich gezielt mit der Stärkung des Selbstkonzepts, der Resilienz sowie dem Selbstwert auseinander. Wir stellen dabei die Anliegen der Klienten in den Fokus.
Das Angebot basiert auf dem Konzept des Lernfeld Frohsinn des Kurt- Lambrecht-Institut, Heidelberg
Aufgabenstellung
Die Inhalte der Fortbildung sollen enthalten sein.
Layout sollte unseren Arbeitsbereich im psychologischen Wohlbefinden widerspiegeln

```html
<!DOCTYPE html>
<html lang="de">
<head>
<meta charset="utf-8">
<title>Heiterwerk – Fortbildung für Beratungslehrer</title>
<link rel="stylesheet" href="https://fonts.googleapis.com/css2?family=Montserrat:wght@500;600;700&family=Open+Sans:wght@400;600;700&display=swap">
<style>
  :root{
    --teal:#2e8f82;
    --teal-dark:#237468;
    --teal-light:#5fb3a5;
    --ink:#4a4a4a;
    --grey:#7a7a7a;
    --paper:#ffffff;
    --bg:#ffffff;
  }
  *{box-sizing:border-box;margin:0;padding:0}
  html,body{width:814px;height:1200px;overflow:hidden;background:var(--bg)}
  body{position:relative;font-family:"Open Sans",Arial,sans-serif;color:var(--ink)}
  .spread{position:absolute;left:57px;width:700px;height:530px;display:flex;box-shadow:0 2px 10px rgba(0,0,0,.18)}
  .spread--outer{top:22px}
  .spread--inner{top:632px}
  .page{position:relative;width:350px;height:530px;background:var(--paper);overflow:hidden}
  .page + .page{border-left:1px solid #e6e6e6}
  .page svg.bg{position:absolute;left:0;top:0}
  .brand{position:absolute;display:flex;align-items:center;gap:6px;font-family:"Montserrat",sans-serif;font-weight:600;font-size:10px;letter-spacing:.12em;text-transform:uppercase}
  .brand__dot{width:24px;height:24px;border-radius:50%;border:1.5px solid currentColor}
  .brand--light{color:#fff;left:50%;top:52px;transform:translateX(-50%)}
  .brand--teal{color:var(--teal);left:30px;top:34px}
  .back__contact{position:absolute;left:30px;bottom:34px;font-size:10px;line-height:1.4;color:#222}
  .back__contact strong{display:block;font-weight:700}
  .cover__title{position:absolute;left:40px;top:106px;width:280px;font-family:"Montserrat",sans-serif;font-weight:700;font-size:12.5px;line-height:1.35;color:var(--teal);text-transform:uppercase}
  .cover__sub{position:absolute;left:40px;top:160px;font-family:"Montserrat",sans-serif;font-weight:600;font-size:13px;color:var(--teal)}
  .cover__desc{position:absolute;left:40px;top:182px;width:240px;font-size:10px;line-height:1.35;color:var(--grey)}
  .intro{position:absolute;left:28px;top:16px;width:280px;color:#fff;font-size:9px;line-height:1.4;font-weight:600}
  .column{position:absolute;left:28px;width:294px}
  .column--left{top:122px}
  .column--right{top:108px}
  .column h2{font-family:"Montserrat",sans-serif;font-weight:700;font-size:11px;color:var(--teal);text-transform:uppercase;margin:0 0 8px;letter-spacing:.02em}
  .column p{font-size:8.5px;line-height:1.5;margin-bottom:16px}
  .column h3{font-size:8.5px;font-weight:600;color:var(--teal);margin-bottom:2px}
  .column .item p{margin-bottom:9px}
  .tab{position:absolute;right:22px;top:16px;color:#fff;font-size:8.5px;font-family:"Montserrat",sans-serif;font-weight:500}
  .cta{position:absolute;left:28px;top:445px;width:240px;color:#fff;font-family:"Montserrat",sans-serif;font-weight:600;font-size:11.5px;line-height:1.4}
</style>
</head>
<body>

<section class="spread spread--outer">
  <article class="page page--back">
    <svg class="bg" width="350" height="530" viewBox="0 0 350 530">
      <polygon points="0,0 350,0 350,385 0,430" fill="var(--teal)"/>
    </svg>
    <div class="brand brand--light"><span class="brand__dot"></span>Heiterwerk</div>
    <p class="back__contact"><strong>Mehr Informationen auf</strong>www.heiterwerk.de</p>
  </article>

  <article class="page page--cover">
    <svg class="bg" width="350" height="530" viewBox="0 0 350 530">
      <defs>
        <linearGradient id="forest" x1="0" y1="0" x2="0" y2="1">
          <stop offset="0" stop-color="#6e8f3a"/>
          <stop offset="0.45" stop-color="#3f6a2c"/>
          <stop offset="0.7" stop-color="#2f8f86"/>
          <stop offset="1" stop-color="#1f6f73"/>
        </linearGradient>
      </defs>
      <polygon points="0,255 350,215 350,472 0,500" fill="url(#forest)" role="img" aria-label="Foto: Waldlichtung mit klarem, türkisfarbenem Bach"/>
      <polygon points="0,500 350,472 350,530 0,530" fill="var(--teal)"/>
    </svg>
    <div class="brand brand--teal"><span class="brand__dot"></span>Heiterwerk</div>
    <h1 class="cover__title">Stärkung des Selbstkonzepts, des Selbstwerts und der Resilienz</h1>
    <p class="cover__sub">Fortbildung für Beratungslehrer</p>
    <p class="cover__desc">Stärkung des Selbstkonzepts, des Selbstwerts und der Resilienz</p>
  </article>
</section>

<section class="spread spread--inner">
  <article class="page page--inside-left">
    <svg class="bg" width="350" height="530" viewBox="0 0 350 530">
      <polygon points="0,0 350,0 350,70 0,100" fill="var(--teal)"/>
    </svg>
    <p class="intro">Sie sind Beratungslehrer und möchten Ihre Schüler*innen bestmöglich in ihrer persönlichen Entwicklung unterstützen? Dann ist diese Fortbildung genau das Richtige für Sie!</p>
    <div class="column column--left">
      <h2>Inhalt der Fortbildung</h2>
      <p>In dieser praxisorientierten Fortbildung lernen Sie, wie Sie Ihre Klient*innen gezielt in den Bereichen Selbstkonzept, Selbstwert und Resilienz stärken können. Basierend auf dem bewährten Konzept des Lernfeld Frohsinn werden Ihnen Methoden und Techniken vermittelt, die direkt in der Beratung anwendbar sind.</p>
      <h2>Was erwartet Sie?</h2>
      <div class="item"><h3>1. Stärkung des Selbstkonzepts</h3><p>Erfahren Sie, wie Sie Klient*innen helfen können, ein gesundes und positives Selbstbild zu entwickeln.</p></div>
      <div class="item"><h3>2. Aufbau von Selbstwert</h3><p>Entdecken Sie Wege, um das Selbstvertrauen und die Eigenmotivation Ihrer Klient*innen nachhaltig zu fördern.</p></div>
      <div class="item"><h3>3. Förderung der Resilienz</h3><p>Lernen Sie Strategien kennen, mit denen Klient*innen Krisen und Herausforderungen besser bewältigen können.</p></div>
    </div>
  </article>

  <article class="page page--inside-right">
    <svg class="bg" width="350" height="530" viewBox="0 0 350 530">
      <polygon points="0,0 350,0 350,48 0,78" fill="var(--teal-light)" opacity=".35"/>
      <polygon points="150,0 350,0 350,42 170,58" fill="var(--teal)"/>
      <polygon points="0,438 350,398 350,530 0,530" fill="var(--teal)"/>
    </svg>
    <span class="tab">Information</span>
    <div class="column column--right">
      <h2>Warum das Lernfeld Frohsinn?</h2>
      <p>Das Lernfeld Frohsinn verbindet positive Psychologie mit pädagogischen Ansätzen und ermöglicht eine ganzheitliche Förderung der Persönlichkeit. Ziel ist es, Klient*innen auf ein erfülltes und selbstbestimmtes Leben vorzubereiten.</p>
      <h2>Für wen ist die Fortbildung geeignet?</h2>
      <p>Diese Fortbildung richtet sich an Beratungslehrer, Schulpsychologen und pädagogische Fachkräfte, die ihre Kompetenzen erweitern und ihre Klient*innen bestmöglich unterstützen möchten.</p>
    </div>
    <p class="cta">Investieren Sie in die Zukunft Ihrer Klient*innen – und in Ihre eigene Weiterbildung!</p>
  </article>
</section>

</body>
</html>
```